Cedar Hollow Resort & Marina - Boat Slips, Cabin Rentals, Floating Vacation Homes, & More

We need an 8'H x 16'W billboard for our Resort & marina, www.cedarhollowresort.example. We'd like it to include: Lakefront Cabin Rentals, Floating Vacation Homes, and New Slips Summer 2022. We'd like it to be simple using the colors on our logo, similar to our business cards, and have our logo on it large. Maybe an arrow on the bottom pointing left that says 3 miles, possibly our website and phone number.

Target Market(s)

Lake People, Boaters

Industry/Entity Type

Resort & Marina (Recreation/Hospitality)

Font styles to use
Sans Serif
Other font styles liked:
• Simple/modern

Colors
0054AA
0677BA
7BADD7
CADEEF
E8F1F8
FFC000
F8CF3A
FAE287
FDF2CF
FEFAEE
F0912C
F2A743
F7CA91
FBE8D2
FDF5EE

Requirements
Must have
• Logo, Cabin Rentals, Floating Vacation Homes, New Slips Summer 2022
Nice to have
• An additional banner hanging from the bottom with an orange (or blue, colors from our logo) arrow pointing left, with white text saying: 3 miles 555-214-6873 www.cedarhollowresort.example
Should not have
• Shouldn't be too busy

```html
<!DOCTYPE html>
<html lang="en">
<head>
<meta charset="utf-8">
<title>Cedar Hollow Resort &amp; Marina Billboard</title>
<link rel="stylesheet" href="https://fonts.googleapis.com/css2?family=Tinos:wght@400;700&display=swap">
<style>
  :root {
    --page: #fefefe;
    --panel: #e1e5ee;
    --navy: #134c84;
    --accent-orange: #f2a743;
    --arrow-red: #e9553a;
    --sun-yellow: #ffc000;
    --white: #ffffff;
    --frame: #555b66;
  }
  html, body {
    margin: 0;
    padding: 0;
    width: 1200px;
    height: 1200px;
    overflow: hidden;
    background: var(--page);
  }
  .canvas {
    position: relative;
    width: 1200px;
    height: 1200px;
    font-family: "Tinos", "Times New Roman", serif;
  }
  .billboard {
    position: absolute;
    left: 61px;
    top: 427px;
    width: 1080px;
    height: 315px;
    background: var(--panel);
    outline: 1px solid var(--frame);
    overflow: hidden;
  }
  .features {
    position: absolute;
    left: 52px;
    top: 22px;
    margin: 0;
    padding: 0;
    list-style: none;
  }
  .features li {
    position: relative;
    padding-left: 29px;
    font-size: 36px;
    line-height: 47px;
    color: var(--navy);
    white-space: nowrap;
  }
  .features li::before {
    content: "";
    position: absolute;
    left: 0;
    top: 17px;
    width: 17px;
    height: 17px;
    border-radius: 50%;
    background: linear-gradient(to bottom, var(--sun-yellow), var(--arrow-red));
  }
  .distance {
    position: absolute;
    left: 51px;
    top: 166px;
    display: flex;
    align-items: center;
    gap: 10px;
  }
  .distance-label {
    font-weight: 700;
    font-size: 52px;
    line-height: 1;
    color: var(--arrow-red);
    white-space: nowrap;
  }
  .brand-name {
    position: absolute;
    left: 530px;
    width: 520px;
    top: 118px;
    text-align: center;
    color: var(--navy);
    font-weight: 400;
  }
  .brand-name .primary {
    display: block;
    font-size: 58px;
    line-height: 1;
    letter-spacing: 1px;
  }
  .brand-name .secondary {
    display: block;
    margin-top: 8px;
    font-size: 24px;
    letter-spacing: 9px;
  }
  .rule {
    position: absolute;
    left: 0;
    right: 0;
    top: 227px;
    height: 4px;
    background: var(--accent-orange);
  }
  .contact-band {
    position: absolute;
    left: 0;
    right: 0;
    bottom: 0;
    height: 78px;
    background: var(--navy);
    color: var(--white);
    display: flex;
    align-items: center;
    justify-content: space-between;
    padding: 0 36px 0 35px;
    font-size: 46px;
    white-space: nowrap;
  }
</style>
</head>
<body>
<div class="canvas">
  <section class="billboard">
    <ul class="features">
      <li>Lakefront Cabin Rentals</li>
      <li>Floating Vacation Homes</li>
      <li>New Slips Summer 2022</li>
    </ul>

    <div class="distance">
      <svg class="distance-arrow" width="122" height="52" viewBox="0 0 122 52" aria-hidden="true">
        <polygon points="0,26 50,0 50,15 122,15 122,37 50,37 50,52" fill="var(--arrow-red)"/>
      </svg>
      <span class="distance-label">3 Miles</span>
    </div>

    <div class="brand-name">
      <span class="primary">CEDAR HOLLOW</span>
      <span class="secondary">RESORT &amp; MARINA</span>
    </div>

    <div class="rule"></div>

    <div class="contact-band">
      <span class="phone">Call: 555-214-6873</span>
      <span class="website">www.cedarhollowresort.example</span>
    </div>
  </section>
</div>
</body>
</html>
```